BRIARFELL Real Estate
Real Estate Developer
Project: BRIARFELL Real Estate
BRIARFELL Real Estate - Real Estate
Creative Brief
Use specific fonts
Up to the designer!
Professional
Matthias L. Halvik
Managing Director
BRIARFELL Real Estate GmbH & Co. KG Lindauer Gang 14 20417 Hamburg Germany
mlh@briarfellre.com
briarfellre.com
One-sided or two-sided cards are welcome and any of the three logos and its colour variations can be chosen!

```html
<!DOCTYPE html>
<html lang="en">
<head>
<meta charset="utf-8">
<title>BRIARFELL Real Estate – Business Card</title>
<link rel="stylesheet" href="https://fonts.googleapis.com/css2?family=Montserrat:wght@500;700;800&family=Roboto:wght@400;500;700&display=swap">
<style>
  :root {
    --green-deep: #1f4a2c;
    --green: #2a5e38;
    --green-light: #3f7a4d;
    --ink: #2b2b2b;
    --ink-soft: #555a57;
    --paper: #ffffff;
    --paper-shade: #eef1ef;
    --stage: #d9dcda;
  }
  * { box-sizing: border-box; margin: 0; padding: 0; }
  html, body {
    width: 1200px; height: 871px; overflow: hidden;
    background: var(--stage);
  }
  .stage {
    width: 1200px; height: 871px;
    display: flex; flex-direction: column; align-items: center; justify-content: center;
    gap: 40px;
  }
  .card {
    width: 620px; height: 377px; border-radius: 18px;
    position: relative; overflow: hidden;
    box-shadow: 0 10px 28px rgba(0,0,0,.22);
  }

  /* Back side */
  .card-back {
    background: linear-gradient(135deg, var(--green-light) 0%, var(--green) 45%, var(--green-deep) 100%);
    color: var(--paper);
  }
  .card-back .deco-circle {
    position: absolute; right: -60px; top: -40px;
    width: 380px; height: 380px; border-radius: 50%;
    background: rgba(255,255,255,.92);
  }
  .card-back .brand {
    position: absolute; left: 44px; bottom: 92px;
  }
  .card-back .brand-name {
    font-family: "Montserrat", sans-serif; font-weight: 800;
    font-size: 44px; letter-spacing: 1px; line-height: 1;
  }
  .card-back .brand-tag {
    font-family: "Montserrat", sans-serif; font-weight: 500;
    font-size: 15px; letter-spacing: 6px; margin-top: 6px; padding-left: 120px;
  }
  .card-back .web {
    position: absolute; left: 44px; bottom: 40px;
    font-family: "Roboto", sans-serif; font-size: 15px; letter-spacing: 3px;
    opacity: .9;
  }

  /* Front side */
  .card-front {
    background: linear-gradient(160deg, var(--paper) 60%, var(--paper-shade) 100%);
    color: var(--ink);
  }
  .logo-block {
    position: absolute; left: 40px; top: 96px; width: 250px;
    display: flex; flex-direction: column; align-items: center;
  }
  .logo-dot {
    width: 52px; height: 52px; border-radius: 50%;
    background: var(--green); margin-bottom: 10px;
  }
  .logo-name {
    font-family: "Montserrat", sans-serif; font-weight: 800;
    font-size: 38px; color: var(--green); line-height: 1; letter-spacing: .5px;
  }
  .logo-tag {
    font-family: "Montserrat", sans-serif; font-weight: 500;
    font-size: 14px; color: var(--green); letter-spacing: 6px; margin-top: 6px;
    align-self: flex-end;
  }
  .divider {
    position: absolute; left: 312px; top: 44px; width: 1px; height: 236px;
    background: #c9cfcb;
  }
  .details {
    position: absolute; left: 334px; top: 46px;
    font-family: "Roboto", sans-serif;
  }
  .person-name { font-size: 20px; font-weight: 700; color: var(--green); }
  .person-title { font-size: 13px; font-weight: 700; color: var(--ink); margin-top: 4px; }
  .address { font-size: 13px; color: var(--ink-soft); margin-top: 18px; line-height: 1.45; }
  .contacts { list-style: none; margin-top: 16px; font-size: 13px; color: var(--ink-soft); }
  .contacts li { display: flex; align-items: center; gap: 10px; height: 20px; }
  .contacts svg { width: 14px; height: 14px; fill: var(--ink-soft); flex: none; }
  .band {
    position: absolute; left: 0; right: 0; bottom: 54px; height: 34px;
    background: var(--green);
    display: flex; align-items: center; padding-left: 150px;
    font-family: "Roboto", sans-serif; font-size: 15px; letter-spacing: 3px; color: var(--paper);
  }
  .band-dot {
    position: absolute; right: 36px; bottom: 8px;
    width: 32px; height: 32px; border-radius: 50%; background: var(--ink-soft);
  }
</style>
</head>
<body>
<main class="stage">
  <section class="card card-back" aria-label="Business card back">
    <div class="deco-circle"></div>
    <div class="brand">
      <div class="brand-name">BRIARFELL</div>
      <div class="brand-tag">REAL ESTATE</div>
    </div>
    <div class="web">www.briarfellre.com</div>
  </section>

  <section class="card card-front" aria-label="Business card front">
    <div class="logo-block">
      <div class="logo-dot"></div>
      <div class="logo-name">BRIARFELL</div>
      <div class="logo-tag">REAL ESTATE</div>
    </div>
    <div class="divider"></div>
    <div class="details">
      <div class="person-name">Matthias L. Halvik</div>
      <div class="person-title">Managing Director</div>
      <div class="address">Lindauer Gang 14<br>20417 Hamburg, Germany</div>
      <ul class="contacts">
        <li><svg viewBox="0 0 24 24"><path d="M6.6 10.8a15 15 0 0 0 6.6 6.6l2.2-2.2c.3-.3.7-.4 1-.2 1.1.4 2.3.6 3.6.6.6 0 1 .4 1 1V20c0 .6-.4 1-1 1A17 17 0 0 1 3 4c0-.6.4-1 1-1h3.5c.6 0 1 .4 1 1 0 1.3.2 2.5.6 3.6.1.3 0 .7-.2 1z"/></svg>+49 (0)40 5550182</li>
        <li><svg viewBox="0 0 24 24"><path d="M7 1h10a2 2 0 0 1 2 2v18a2 2 0 0 1-2 2H7a2 2 0 0 1-2-2V3a2 2 0 0 1 2-2zm0 3v14h10V4zm5 15.5a1 1 0 1 0 0 2 1 1 0 0 0 0-2z"/></svg>+49 (0)175 5550947</li>
        <li><svg viewBox="0 0 24 24"><path d="M6 2h9l3 3v4h1a3 3 0 0 1 3 3v7h-4v3H6v-3H2v-7a3 3 0 0 1 3-3h1zm2 2v5h8V6h-2V4zm0 12v4h8v-4z"/></svg>+49 (0)40 5550183</li>
        <li><svg viewBox="0 0 24 24"><path d="M2 5h20v14H2zm2 2v.4l8 5 8-5V7zm0 2.8V17h16V9.8l-8 5z"/></svg>mlh@briarfellre.com</li>
      </ul>
    </div>
    <div class="band">www.briarfellre.com</div>
    <div class="band-dot"></div>
  </section>
</main>
</body>
</html>
```